BrovaNest Landing Web Page

We need a web design for a new company head quartered in Philadelphia, PA with satellite offices in San Francisco, CA and New York, NY.
We have a logo and can provide the logo image file.
Here is some information on who we are:
BrovaNest
Growing information technology companies with experience
About Us: BrovaNest is an information technology incubator. We cultivate and groom start-ups from concept to reality to profitability. BrovaNest is managed and owned by entrepreneurs and technologists with proven start-up success. We seek to leverage synergies between our companies which foster innovation, stimulate creativity, increase productivity, streamline operational processes, and facilitate opportunity.
BrovaNest Companies:
• BrovaNest Health (should hyperlink to BrovaNest Health About Us section)
• BrovaNest IT Services and Staffing (should hyperlink to BrovaNest IT Services and Staffing About Us section)
Healthcare
Information Technology

```html
<!DOCTYPE html>
<html lang="en">
<head>
<meta charset="utf-8">
<title>BrovaNest</title>
<link href="https://fonts.googleapis.com/css2?family=Arimo:wght@400;700&display=swap" rel="stylesheet">
<style>
  :root {
    --brand-teal: #2bb3d6;
    --brand-blue: #1b6fae;
    --it-light: #2a9ce6;
    --it-dark: #0f6fb8;
    --health-light: #3dd6ee;
    --health-dark: #22a9c6;
    --heading: #5e3b8e;
    --heading-soft: #8b6cb3;
    --body: #555;
    --body-soft: #777;
    --footer-light: #7fc2ea;
    --footer-dark: #1690e0;
    --white: #fff;
  }
  * { box-sizing: border-box; margin: 0; padding: 0; }
  html, body { width: 1200px; height: 696px; overflow: hidden; background: var(--white); }
  body { position: relative; font-family: "Arimo", Helvetica, Arial, sans-serif; }

  .header-logo {
    position: absolute; left: 450px; top: 0; width: 296px; height: 119px;
    background: var(--white); border-radius: 0 0 3px 3px;
    box-shadow: 0 2px 6px rgba(0,0,0,.3); z-index: 2;
    display: flex; align-items: center; justify-content: center; gap: 12px;
  }
  .logo-dot { width: 34px; height: 34px; border-radius: 50%; background: var(--brand-teal); }
  .logo-name { font-size: 36px; font-weight: 700; color: var(--brand-teal); letter-spacing: .5px; }

  .division {
    position: absolute; top: 79px; height: 295px; text-decoration: none; color: var(--white);
  }
  .division-it {
    left: 0; width: 594px; border-radius: 0 0 6px 0;
    background: linear-gradient(180deg, var(--it-light) 0%, var(--it-dark) 100%);
  }
  .division-health {
    left: 607px; width: 593px; border-radius: 0 0 0 6px;
    background: linear-gradient(100deg, var(--health-light) 0%, #4fd0e6 50%, var(--health-dark) 100%);
  }
  .division-photo { position: absolute; top: 0; height: 100%; }
  .division-it .division-photo {
    left: 0; width: 370px;
    background: linear-gradient(90deg, #3a4450 0%, #5a6a78 60%, rgba(42,156,230,0) 100%);
  }
  .division-health .division-photo {
    right: 0; width: 250px;
    background: linear-gradient(270deg, #c9d8df 0%, #b6e7f1 60%, rgba(61,214,238,0) 100%);
  }
  .division-title {
    position: absolute; top: 125px; font-weight: 700; line-height: 1; color: rgba(255,255,255,.92);
  }
  .division-it .division-title { right: 44px; text-align: right; }
  .division-health .division-title { left: 43px; }
  .division-title .brand { display: block; font-size: 27px; letter-spacing: .3px; }
  .division-title .sector { display: block; font-size: 44px; margin-top: 2px; }

  .intro {
    position: absolute; top: 415px; left: 153px; display: flex;
  }
  .intro-column { width: 239px; margin-right: 37px; }
  .intro-column:nth-child(2) { margin-right: 41px; }
  .intro-column.wide { width: 375px; margin-right: 0; }
  .intro-heading { font-size: 16.5px; font-weight: 400; color: var(--heading); margin-bottom: 11px; }
  .intro-column:first-child .intro-heading { color: var(--heading-soft); }
  .intro-text { font-size: 11.6px; line-height: 18.75px; color: var(--body); text-align: justify; }
  .intro-column:first-child .intro-text { color: var(--body-soft); }
  .intro-text + .intro-text { margin-top: 18.75px; }

  .site-footer {
    position: absolute; left: 0; top: 628px; width: 1200px; height: 68px;
    background: linear-gradient(90deg, var(--footer-light) 0%, #4fa8e3 25%, var(--footer-dark) 45%, var(--footer-dark) 100%);
  }
  .footer-links {
    position: absolute; left: 386px; top: 24px; display: flex; list-style: none;
    font-size: 13px; color: var(--white);
  }
  .footer-links li + li::before { content: "|"; margin: 0 14px; }
  .footer-links a { color: var(--white); text-decoration: none; }
  .social-links { position: absolute; left: 867px; top: 16px; display: flex; gap: 26px; list-style: none; }
  .social-links span {
    display: block; width: 22px; height: 22px; border: 2px solid rgba(255,255,255,.9); border-radius: 50%;
  }
</style>
</head>
<body>
  <header class="header-logo">
    <span class="logo-dot"></span>
    <span class="logo-name">BrovaNest</span>
  </header>

  <a class="division division-it" href="#it-services-about">
    <div class="division-photo" role="img" aria-label="Photo of a smiling man working on a laptop"></div>
    <h2 class="division-title"><span class="brand">BROVANEST</span><span class="sector">IT</span></h2>
  </a>

  <a class="division division-health" href="#health-about">
    <div class="division-photo" role="img" aria-label="Photo of a doctor with a stethoscope holding a clipboard"></div>
    <h2 class="division-title"><span class="brand">BROVANEST</span><span class="sector">HEALTH</span></h2>
  </a>

  <main class="intro">
    <section class="intro-column">
      <h3 class="intro-heading">LOREM IPSUM IS SIMPLY</h3>
      <p class="intro-text">Lorem Ipsum is simply dummy text of the printing and typesetting industry. Lorem Ipsum has been the industry's standard dummy text ever since the 1500s, when an unknown printer took a galley of type and scrambled it to make a type specimen book. It has survived not only five centuries, but also the leap into electronic typesetting, remaining essentially unchanged.</p>
    </section>
    <section class="intro-column">
      <h3 class="intro-heading">LOREM IPSUM IS SIMPLY</h3>
      <p class="intro-text">Lorem Ipsum is simply dummy text of the printing and typesetting industry. Lorem Ipsum has been the industry's standard dummy text ever since the 1500s, when an unknown printer took a galley of type and scrambled it to make a type specimen book. It has survived not only five centuries, but also the leap into electronic typesetting, remaining essentially unchanged.</p>
    </section>
    <section class="intro-column wide">
      <h3 class="intro-heading">LOREM IPSUM IS SIMPLY</h3>
      <p class="intro-text">Lorem Ipsum is simply dummy text of the printing and typesetting industry. Lorem Ipsum has been the industry's standard dummy text ever since the 1500s, when an unknown printer took a galley of type and scrambled it to make a type specimen book. It has survived not only five centuries, but also the leap into electronic typesetting, remaining essentially unchanged.</p>
      <p class="intro-text">It was popularised in the 1960s with the release of Letraset sheets containing Lorem Ipsum passages, and more recently with</p>
    </section>
  </main>

  <footer class="site-footer">
    <ul class="footer-links">
      <li><a href="#terms">Terms of Use</a></li>
      <li><a href="#accessibility">Accessibility</a></li>
      <li><a href="#privacy">Privacy</a></li>
      <li><a href="#signup">Email Sign Up</a></li>
    </ul>
    <ul class="social-links" aria-label="Social links">
      <li><span></span></li>
      <li><span></span></li>
      <li><span></span></li>
      <li><span></span></li>
    </ul>
  </footer>
</body>
</html>
```